Develop new wine label for entry level Greek wines **

We need a label design for the new line of entry level Greek wines.

We will have 4 SKU: red dry wine, red semi sweet wine, white dry wine, white semi-sweet wines.

We would like to see traditional greek houses on it.

There needs to be a slight colour difference between dry and semi sweet wines (you can maybe change colours of some details in order to differentiate wines on the shelf).

We would like to use designs that use white and blue colours (I attached some images for your inspiration). The glass bottle will be transparent so keep in mind how the label will coordinate with the colour of the wine itself.

The label needs to communicate that the wine is from Greece, this wine is simple, approachable, easy to drink, modern and fun.

The brand name is the ancient Greek word "velmara". Quoting knowlia: " Velmara (ancient Greek: βέλμαρα, plural: βέλμαρες; English prefix: eco- for ecology and economics) refers to three related but distinct concepts: the family, the family's property, and the house.".

So feel free to further elaborate on the concept.

The text that should appear on the label:
1. Brand name - Velmara (a good idea would be to use a greek style shrift would be great to mimic greek letters βέλμαρα).
2. White semi-sweet / White dry / Red semi-sweet / Red dry

Target Market(s)

Ukraine

Font styles to use
Serif

Colors
33a6d7
cee9f5
ffffff
e34297

Requirements
Must have
• The customer needs to look at the bottle and understand that is it from Greece straight away.

```html
<!DOCTYPE html>
<html lang="en">
<head>
<meta charset="utf-8">
<title>Velmara Greek Wine Label</title>
<link href="https://fonts.googleapis.com/css2?family=Allura&family=Cinzel:wght@700&family=Cormorant+Garamond:wght@400;500;600&family=Oswald:wght@400;500&display=swap" rel="stylesheet">
<style>
  :root {
    --backdrop: #e4e4e6;
    --label: #ffffff;
    --ink: #2a2626;
    --aegean: #33a6d7;
    --aegean-pale: #cee9f5;
    --magenta: #e34297;
    --grey: #7d8a91;
  }
  * { margin: 0; padding: 0; box-sizing: border-box; }
  html, body {
    width: 1200px; height: 799px; overflow: hidden;
    background: var(--backdrop);
  }
  .canvas {
    position: relative; width: 1200px; height: 799px;
    display: flex; justify-content: center; align-items: center;
  }
  .label {
    position: relative; width: 400px; height: 720px;
    background: var(--label);
    box-shadow: 0 6px 24px rgba(0,0,0,0.10);
    color: var(--ink);
    text-align: center;
  }
  .label__kicker {
    position: absolute; top: 22px; left: 0; right: 0;
    font-family: "Allura", cursive; font-size: 52px; line-height: 1;
  }
  .label__brand {
    position: absolute; top: 92px; left: 0; right: 0;
    font-family: "Cinzel", serif; font-weight: 700;
    font-size: 50px; letter-spacing: 3px; line-height: 1;
  }
  .label__rule {
    position: absolute; top: 146px; left: 100px; width: 200px; height: 3px;
    background: var(--aegean);
  }
  .label__scene {
    position: absolute; top: 164px; left: 100px; width: 200px; height: 204px;
    background: radial-gradient(ellipse at center, var(--aegean-pale) 0%, #e9f5fb 60%, var(--label) 100%);
  }
  .label__spec {
    position: absolute; top: 278px;
    font-family: "Oswald", sans-serif; font-size: 15px; color: var(--grey);
    letter-spacing: 0.3px;
  }
  .label__spec--volume { left: 40px; }
  .label__spec--abv { right: 20px; }
  .label__wine {
    position: absolute; top: 424px; left: 0; right: 0;
    font-family: "Cormorant Garamond", serif; font-weight: 600;
    font-size: 60px; line-height: 1; color: var(--magenta);
    letter-spacing: 2px;
  }
  .label__tagline {
    position: absolute; top: 534px; left: 0; right: 0;
    font-family: "Cormorant Garamond", serif; font-size: 12px;
    letter-spacing: 3px; color: var(--grey);
  }
  .label__maker {
    position: absolute; top: 552px; left: 0; right: 0;
    font-family: "Allura", cursive; font-size: 26px; color: var(--ink);
  }
  .label__since {
    position: absolute; top: 596px; left: 0; right: 0;
    display: flex; justify-content: center; align-items: center; gap: 14px;
  }
  .label__leaf {
    width: 44px; height: 46px; background: var(--aegean); border-radius: 50% 50% 45% 45%;
  }
  .label__year {
    font-family: "Oswald", sans-serif; font-weight: 500; font-size: 26px;
    line-height: 1.15; color: var(--aegean);
  }
  .label__band {
    position: absolute; left: 0; right: 0; bottom: 0; height: 58px;
    background: var(--aegean);
    display: flex; flex-direction: column; justify-content: center;
    font-family: "Cormorant Garamond", serif; font-size: 9px;
    color: #ffffff; letter-spacing: 0.6px; line-height: 1.4;
  }
</style>
</head>
<body>
<main class="canvas">
  <section class="label">
    <p class="label__kicker">Greek Wine</p>
    <h1 class="label__brand">VELMARA</h1>
    <div class="label__rule"></div>
    <div class="label__scene" role="img" aria-label="Sketch of traditional white Greek houses with blue doors"></div>
    <span class="label__spec label__spec--volume">750 ML</span>
    <span class="label__spec label__spec--abv">ALC. 11,5%</span>
    <p class="label__wine">RED DRY</p>
    <p class="label__tagline">SIMPLE &amp; EASY TO DRINK</p>
    <p class="label__maker">βέλμαρα · family house</p>
    <div class="label__since">
      <div class="label__leaf" role="img" aria-label="Vine leaf ornament"></div>
      <p class="label__year">SINCE<br>1964</p>
      <div class="label__leaf" role="img" aria-label="Vine leaf ornament"></div>
    </div>
    <footer class="label__band">
      <span>Grown on sunny Greek hills, bottled young for easy,</span>
      <span>fresh and bright everyday drinking with friends.</span>
    </footer>
  </section>
</main>
</body>
</html>
```